Brennick Holdings Business Cards

These are professional business cards that are for my family office.
Put fake emails and phone numbers as of now until I finalize those components. This family office controls my families investments, assets, and future. The cards should be professional.
..
.
.
.
I just uploaded another variation of a logo I would like to see as a business card to I am inbeteen which logo to use

Target Market(s)

business

Industry/Entity Type

business

Contact Information for Business Card

Professional, wealth related, finance related.

Requirements
Must have
• Logo

```html
<!DOCTYPE html>
<html lang="en">
<head>
<meta charset="utf-8">
<title>Brennick Holdings — Business Cards</title>
<link rel="stylesheet" href="https://fonts.googleapis.com/css2?family=Playfair+Display:wght@400&family=Tinos:wght@400;700&display=swap">
<style>
  :root {
    --backdrop: #a4a4a4;
    --card-light: #f1f1f2;
    --card-mid: #e8e9eb;
    --ink: #1f1c1d;
    --icon-fg: #ffffff;
  }
  * { box-sizing: border-box; margin: 0; padding: 0; }
  html, body { width: 1200px; height: 1200px; overflow: hidden; }
  body {
    background: var(--backdrop);
    position: relative;
    font-family: "Tinos", "Times New Roman", serif;
    color: var(--ink);
  }
  .card {
    position: absolute;
    left: 272px;
    width: 655px;
    height: 374px;
    overflow: hidden;
  }
  .card--front { top: 212px; }
  .card--back { top: 614px; }
  .card__pattern {
    position: absolute;
    inset: 0;
    background: linear-gradient(180deg, var(--card-light) 0%, var(--card-mid) 50%, var(--card-light) 100%);
  }

  .holder { position: absolute; left: 50px; top: 152px; }
  .holder__name {
    font-weight: 700;
    font-size: 30px;
    line-height: 1;
    padding-bottom: 3px;
    border-bottom: 1px solid var(--ink);
    width: 199px;
    white-space: nowrap;
  }
  .holder__role { font-size: 25px; line-height: 1; margin-top: 6px; }

  .contact { position: absolute; left: 327px; top: 66px; list-style: none; }
  .contact__item {
    display: flex;
    align-items: center;
    height: 38px;
    margin-bottom: 9px;
    font-size: 24px;
    white-space: nowrap;
  }
  .contact__icon { width: 38px; height: 38px; margin-right: 11px; flex: none; }

  .address { position: absolute; left: 329px; top: 260px; display: flex; align-items: center; }
  .address .contact__icon { margin-right: 18px; }
  .address__lines { font-size: 20px; line-height: 21px; font-style: normal; }

  .accent-bar {
    position: absolute;
    left: 398px;
    right: 0;
    top: 340px;
    height: 10px;
    background: var(--ink);
  }

  .wordmark {
    font-family: "Playfair Display", "Times New Roman", serif;
    font-weight: 400;
    color: var(--ink);
    white-space: nowrap;
    letter-spacing: 0.02em;
  }
  .wordmark--small { position: absolute; left: 20px; top: 330px; font-size: 19px; }
  .wordmark--large {
    position: absolute;
    left: 0;
    right: 0;
    top: 200px;
    text-align: center;
    font-size: 44px;
  }
</style>
</head>
<body>

<section class="card card--front" aria-label="Business card front">
  <div class="card__pattern" role="img" aria-label="Soft grey zigzag background pattern"></div>

  <div class="holder">
    <p class="holder__name">Rowan Ellery</p>
    <p class="holder__role">Designer</p>
  </div>

  <ul class="contact">
    <li class="contact__item">
      <svg class="contact__icon" viewBox="0 0 38 38" aria-hidden="true">
        <circle cx="19" cy="19" r="19" fill="var(--ink)"/>
        <path d="M12 11c1-1 2.5-1 3 0l2 3.5c.5 1 0 1.8-.8 2.4l-1 .8c1 2.3 2.8 4.2 5 5.2l.9-1c.6-.8 1.5-1.2 2.4-.7l3.4 2c1 .6 1 2 0 3l-1.6 1.5c-1.3 1.2-3.3 1.2-5.1.3-4.6-2.3-8.3-6-10.5-10.6-.8-1.8-.8-3.6.4-4.9z" fill="var(--icon-fg)"/>
        <path d="M21 9.5a8 8 0 0 1 7.5 7.5M21 13a4.5 4.5 0 0 1 4 4" stroke="var(--icon-fg)" stroke-width="1.6" fill="none" stroke-linecap="round"/>
      </svg>
      <span>555 204 781 36</span>
    </li>
    <li class="contact__item">
      <svg class="contact__icon" viewBox="0 0 38 38" aria-hidden="true">
        <circle cx="19" cy="19" r="19" fill="var(--ink)"/>
        <g stroke="var(--icon-fg)" stroke-width="1.5" fill="none">
          <circle cx="18" cy="18" r="8.5"/>
          <ellipse cx="18" cy="18" rx="3.8" ry="8.5"/>
          <path d="M9.5 18h17M11 13.5h14M11 22.5h14"/>
        </g>
        <path d="M21 19l7 5.5-3.2.5 1.8 3.5-1.6.8-1.8-3.5-2.2 2.3z" fill="var(--icon-fg)" stroke="var(--ink)" stroke-width=".8"/>
      </svg>
      <span>rowan@brennick.com</span>
    </li>
    <li class="contact__item">
      <svg class="contact__icon" viewBox="0 0 38 38" aria-hidden="true">
        <circle cx="19" cy="19" r="19" fill="var(--ink)"/>
        <g stroke="var(--icon-fg)" stroke-width="1.5" fill="none" stroke-linejoin="round">
          <rect x="10" y="12.5" width="18" height="13"/>
          <path d="M10 12.5l9 7.5 9-7.5M10 25.5l6.5-6.5M28 25.5l-6.5-6.5"/>
        </g>
      </svg>
      <span>www.brennick.com</span>
    </li>
  </ul>

  <div class="address">
    <svg class="contact__icon" viewBox="0 0 38 38" aria-hidden="true">
      <circle cx="19" cy="19" r="19" fill="var(--ink)"/>
      <path d="M19 8a7 7 0 0 1 7 7c0 5.2-7 13.5-7 13.5S12 20.2 12 15a7 7 0 0 1 7-7z" fill="var(--icon-fg)"/>
      <circle cx="19" cy="15" r="2.6" fill="var(--ink)"/>
    </svg>
    <address class="address__lines">Your Address<br>Harbor Lane, Westford,<br>210</address>
  </div>

  <p class="wordmark wordmark--small">BRENNICK HOLDINGS</p>
  <div class="accent-bar"></div>
</section>

<section class="card card--back" aria-label="Business card back">
  <div class="card__pattern" role="img" aria-label="Soft grey zigzag background pattern"></div>
  <p class="wordmark wordmark--large">BRENNICK HOLDINGS</p>
</section>

</body>
</html>
```